MRB - Stationery Design Project

We need stationery based on our logo.

Company info :
Cabinet Morvalle & Associés
Société à responsabilité limitée au capital de 200.000 FCFP
RCS Papeete 27586D - Numéro tahiti C36927
Centre d’affaires OPALE - Rue Gaston Berthelin
BP 51839 MAISON VERDA - 98713 Papeete
Tahiti - Polynésie française
Tél : +689 40 63 17 94
Fax : +689 40 72 39 58

Industry/Entity Type

It Company

Font styles to use
Sans Serif

```html
<!DOCTYPE html>
<html lang="fr">
<head>
<meta charset="utf-8">
<title>MRB – Stationery</title>
<link rel="stylesheet" href="https://fonts.googleapis.com/css2?family=Arimo:wght@400;700&family=Tinos:wght@400;700&display=swap">
<style>
  :root {
    --bg: #262626;
    --paper: #ffffff;
    --navy: #1b3a5c;
    --slate: #7f9393;
    --slate-light: #aab6b6;
    --grey-text: #7a8a8a;
    --ink: #222222;
    --muted: #555555;
    --white: #ffffff;
    --font-body: "Arimo", sans-serif;
    --font-contact: "Tinos", serif;
  }
  * { box-sizing: border-box; margin: 0; padding: 0; }
  html, body { width: 1200px; height: 1092px; overflow: hidden; }
  body { background: var(--bg); position: relative; font-family: var(--font-body); }

  /* Company name in place of the mark */
  .company-name {
    display: flex; align-items: center; gap: 10px;
    font-family: var(--font-body); font-weight: 400;
    color: var(--navy); white-space: nowrap;
  }
  .company-name__square {
    width: 14px; height: 14px; background: var(--slate); flex: none;
  }

  /* Letterhead */
  .letterhead {
    position: absolute; left: 40px; top: 100px;
    width: 620px; height: 877px;
    background: var(--paper);
  }
  .letterhead .company-name {
    position: absolute; left: 44px; top: 80px; font-size: 22px;
  }
  .contact {
    font-family: var(--font-contact); color: var(--ink);
    font-size: 13px; line-height: 1.25;
  }
  .contact b { font-weight: 700; }
  .letterhead .contact { position: absolute; right: 36px; top: 44px; width: 210px; }
  .contact__address { margin-top: 6px; font-size: 11px; color: var(--muted); }

  .letter-body {
    position: absolute; left: 48px; right: 36px; top: 238px;
    font-size: 11px; line-height: 1.3; color: var(--ink);
  }
  .letter-body p { margin-bottom: 12px; }
  .letter-body .qa { margin: 22px 0 0 16px; }
  .letter-body ol { list-style: none; }

  /* Business cards */
  .card { position: absolute; left: 690px; width: 470px; height: 274px; }
  .card--front {
    top: 300px;
    background: linear-gradient(180deg, #ffffff 0%, #f3f4f4 100%);
  }
  .card--front::after {
    content: ""; position: absolute; left: 0; right: 0; bottom: 0;
    height: 14px; background: var(--slate-light);
  }
  .card--front .company-name {
    position: absolute; left: 30px; top: 124px; font-size: 16px;
  }
  .card--front .company-name__square { width: 11px; height: 11px; }
  .card__person { position: absolute; left: 272px; top: 50px; }
  .card__name {
    font-weight: 700; color: var(--grey-text);
    font-size: 21px; background: #f6f7f7; padding: 2px 8px 2px 6px;
  }
  .card__role {
    font-weight: 700; color: var(--muted);
    font-size: 13px; margin: 6px 0 0 6px;
  }
  .card--front .contact {
    position: absolute; left: 278px; top: 145px; font-size: 10.5px; line-height: 1.35;
  }

  .card--back {
    top: 610px; background: var(--slate);
    display: flex; align-items: center; justify-content: center;
  }
  .card--back .company-name { color: var(--white); font-size: 20px; }
  .card--back .company-name__square { background: var(--white); }
</style>
</head>
<body>

<section class="letterhead" aria-label="Papier à en-tête">
  <div class="company-name"><span class="company-name__square"></span>Cabinet Morvalle &amp; Associés</div>
  <div class="contact">
    <div><b>Phone:</b> +689 40 63 17 94</div>
    <div><b>Fax:</b> +689 40 72 39 58</div>
    <div><b>Email:</b> info@morvalle-conseil.pf</div>
    <div><b>Website:</b> www.morvalle-conseil.pf</div>
    <div class="contact__address">Centre d’affaires OPALE - Rue Gaston Berthelin<br>BP 51839 MAISON VERDA - 98713 Papeete</div>
  </div>

  <div class="letter-body">
    <p>Dear<br>Sir/Madam<br>Its all sample text<br>
    A stationary spacetime admits a timelike Killing vector field. A static spacetime is a stationary spacetime in which the timelike Killing vector field has vanishing vorticity, or equivalently (by the Frobenius theorem) is hypersurface orthogonal.</p>
    <p>What does this mean? That a stationary spacetime is one in which you can find a family of observers who observe no changes in the gravitational field (or sources such as matter or electromagnetic fields) over time. A static spacetime is one which admits a slicing into spacelike hypersurfaces which are everywhere orthogonal to the world lines of our "bored observers".</p>
    <p>One can still imagine observers who move around an interact, or even light beams or other waves, which are assumed to have neglible effect on the ambient gravitational field. So for example one can study scattering of waves by black holes.</p>
    <p class="qa">does static imply stationary? is the converse true?</p>
    <p class="qa">Yes. No.</p>
    <p class="qa">What are a couple of example?</p>
    <p class="qa">Some basic examples of static solutions:</p>
    <ol class="qa">
      <li>1. Any Weyl vacuum: see my post #12 in<br>
      http://www.sciforum-notes.net/thread.php?t=153765&amp;highlight=Weyl+vacuum<br>
      plus generalizations allowing for EM fields, scalar fields, etc.</li>
    </ol>
  </div>
</section>

<section class="card card--front" aria-label="Carte de visite, recto">
  <div class="company-name"><span class="company-name__square"></span>Cabinet Morvalle &amp; Associés</div>
  <div class="card__person">
    <div class="card__name">Julien Marchal</div>
    <div class="card__role">Director</div>
  </div>
  <div class="contact">
    <div><b>Phone:</b> +689 40 63 17 94</div>
    <div><b>Fax:</b> +689 40 72 39 58</div>
    <div><b>Email:</b> info@morvalle-conseil.pf</div>
    <div><b>Website:</b> www.morvalle-conseil.pf</div>
  </div>
</section>

<section class="card card--back" aria-label="Carte de visite, verso">
  <div class="company-name"><span class="company-name__square"></span>Cabinet Morvalle &amp; Associés</div>
</section>

</body>
</html>
```